New modern and colorful Brochure for Real Estate shop window/showcase

We are a real estate company in the swiss alps and we need a new design for our (very old fashioned) brochures. Our “word-doc” based “brochure” you’ll find in the attachment.

We need a whole new, modern, clean and colorful design. The key features of a property must be clearly visible, like: (Those key features must be editable)

- 1 main bigger picture of the property
- 4-6 small accompagning Fotos
- Floorplan
- Price
- Property Category
- Buildyear
- Number of rooms
- Number of bathrooms
- Number of bedrooms
- Squaremeter
- Parking place
- Specialities
- Very Short Descripton of the property

We put those brochures in our shop window/showcase, see foto in the attachment. In the attachment you’ll find our business card logo, letterhead logo and on our website www.halvormark-ag.ch another logo.

The new brochure will contain about 4-6 pictures with a main picture of the house, a floorplan and a short description. It must be clearly visible und readable from outside thru a window, so it canot be too small.

Format only A3 in LANDSCAPE.

It must be scalable to A4 to be able to send it to clients (and they will print it to A4)

The brochure must contain our logo with name, subname and year, website, telefon and fax number and address.

To be clear: The whole new brochure will contain only a short description, not like the old design. You can really more concentrate on design and fotos. Description and text will be very short. But we really want to change and no more using the old design...

Just to clarify, the picture with our little agency is just for reference where the new brochures will be. It's jus there to show our window/showcase.

Hope you can help us. Many Greetings and thank you from us!

Project Deadline Extended Reason: Not yet found/submitted "the one". We are missing a more central/important position of the key features of a property. They must be really clearly seen from outside of the window. And we need a two sided A4 "light" version, to hand out to clients. We can't give them a big A3 paper. Scaled down thru the printer isn't the best option. I light version would be optimal....Please continue to submit designs and adopt to the new task, we will reply and give immediate feedback. Thanks a lot! Added Tuesday, January 31, 2017

Reason: still not found the right one

Target Market(s)

Real Estate, Shop Window, Showcase

Industry/Entity Type

Real Estate

Font styles to use
Sans Serif

Colors
0655a3
ec1f27
0293ce
ffc214
e34297

Requirements
Must have
• A3 Format landscape.
• - 1 main bigger picture of the property
• - 4-6 small accompagning Fotos
• - Floorplan
• - Price
• - Property Category
• - Buildyear
• - Number of rooms
• - Number of bathrooms
• - Number of bedrooms
• - Squaremeter
• - Parking place
• - Specialities
• - Short Descripton of the property

```html
<!DOCTYPE html>
<html lang="de">
<head>
<meta charset="utf-8">
<title>Halvormark AG – Appartement</title>
<link href="https://fonts.googleapis.com/css2?family=Source+Sans+3:wght@400;600;700&family=Exo+2:wght@400;600&display=swap" rel="stylesheet">
<style>
  :root{
    --blue:#0655a3;
    --blue-mid:#1f7fc4;
    --sky:#0293ce;
    --red:#ec1f27;
    --yellow:#f6bc18;
    --paper:#f2f2f2;
    --white:#ffffff;
    --plan:#e4e4e4;
    --plan-wall:#9a9a9a;
    --photo-sky:#8fb3dc;
    --photo-snow:#eef2f6;
    --photo-room:#e3dbcc;
    --photo-wood:#d2b68e;
    --photo-tile:#e3d0cc;
  }
  *{margin:0;padding:0;box-sizing:border-box}
  html,body{width:1200px;height:841px;overflow:hidden;background:var(--paper)}
  .brochure{position:relative;width:1200px;height:841px;font-family:"Source Sans 3",sans-serif;overflow:hidden;background:var(--paper)}
  .abs{position:absolute}

  /* left sheet */
  .top-band{left:0;top:0;width:490px;height:22px;background:var(--blue)}
  .corner-tab{left:0;top:0;width:16px;height:60px;background:var(--red)}
  .info-sheet{left:0;top:21px;width:490px;height:820px;background:var(--yellow)}
  .info-edge{left:474px;top:21px;width:16px;height:820px;background:var(--red);border-top-right-radius:12px}

  .brand{left:31px;top:30px;width:170px}
  .brand-dot{width:64px;height:64px;border-radius:50%;background:var(--blue);margin:4px 0 0 48px}
  .brand-name{margin-top:22px;font-family:"Exo 2",sans-serif;font-weight:600;font-size:19px;letter-spacing:1.5px;color:var(--blue);white-space:nowrap}
  .brand-sub{font-family:"Exo 2",sans-serif;font-size:11px;color:var(--blue);white-space:nowrap}

  .contact{left:226px;top:44px;list-style:none;font-family:"Exo 2",sans-serif;font-size:11px;color:var(--blue);line-height:13px}
  .contact li{display:flex;align-items:flex-start;gap:9px;margin-bottom:11px}
  .contact svg{flex:none;width:14px;height:14px}

  .services{left:31px;top:185px;width:420px;display:flex;justify-content:space-between;font-size:12.5px;color:var(--red)}
  .description{left:31px;top:208px;width:420px;font-size:13.6px;line-height:17px;color:var(--blue);text-align:justify}
  .speciality{left:31px;top:366px;font-size:19px;font-weight:700;color:var(--blue)}

  .divider{left:0;top:392px}
  .floorplan{left:33px;top:437px;width:307px;height:385px;background:var(--white);padding:8px}
  .floorplan-area{width:100%;height:100%;background:var(--plan);border:5px solid var(--plan-wall)}
  .spine{left:409px;top:440px;width:2px;height:401px;background:var(--red)}

  .features{left:360px;top:448px;width:104px}
  .feature{position:relative;height:56px;margin-bottom:17px;color:var(--white);text-align:center;padding-top:6px}
  .feature::after{content:"";position:absolute;left:38px;bottom:-14px;border-left:14px solid transparent;border-right:14px solid transparent;border-top:14px solid}
  .feature.dark{background:var(--blue)}
  .feature.dark::after{border-top-color:var(--blue)}
  .feature.light{background:var(--sky)}
  .feature.light::after{border-top-color:var(--sky)}
  .feature-label{font-size:15px;line-height:17px}
  .feature-value{font-size:22px;font-weight:700;line-height:26px}

  /* right sheet */
  .backdrop{left:490px;top:0}
  .photo-main{left:511px;top:51px;width:485px;height:317px;background:linear-gradient(var(--photo-sky),var(--photo-snow))}
  .photo-bedroom{left:512px;top:387px;width:323px;height:238px;background:var(--photo-room)}
  .photo-living{left:849px;top:387px;width:333px;height:238px;background:var(--photo-wood)}
  .photo-dining{left:512px;top:645px;width:224px;height:155px;background:var(--photo-wood)}
  .photo-bath{left:741px;top:645px;width:208px;height:155px;background:var(--photo-tile)}
  .photo-hall{left:954px;top:645px;width:224px;height:155px;background:var(--photo-room)}

  .gold-bar{left:996px;top:0;width:14px;height:387px;background:var(--yellow)}
  .summary{left:1010px;top:0;width:190px;height:387px}
  .summary-text{left:1010px;top:0;width:174px;height:387px;color:var(--white);text-align:center}
  .category{position:absolute;left:0;right:0;top:157px;font-size:26px}
  .year-label{position:absolute;left:0;right:0;top:206px;font-size:11.5px}
  .year{position:absolute;left:0;right:0;top:218px;font-size:25px}
  .area{position:absolute;left:0;right:0;top:256px;font-size:25px;font-weight:700}
  .rule{position:absolute;left:10px;right:10px;top:304px;height:2px;background:var(--white)}
  .price{position:absolute;left:0;right:0;top:322px;font-size:25px;font-weight:700}
  .side-bar{left:1176px;top:625px;width:8px;height:216px;background:var(--sky)}
</style>
</head>
<body>
<main class="brochure">

  <div class="abs top-band"></div>
  <div class="abs info-sheet"></div>
  <div class="abs info-edge"></div>
  <div class="abs corner-tab"></div>

  <div class="abs brand">
    <div class="brand-dot"></div>
    <div class="brand-name">HALVORMARK AG</div>
    <div class="brand-sub">Immobilien und Finanzierungen</div>
  </div>

  <ul class="abs contact">
    <li><svg viewBox="0 0 14 14"><path d="M1 7 7 1.5 13 7h-2v5H8.5V9h-3v3H3V7z" fill="#0655a3"/></svg><span>Postfach 42, Talstrasse 7,<br>CH-3999 Bergmatt</span></li>
    <li><svg viewBox="0 0 14 14"><path d="M1 5c0-2 3-3 6-3s6 1 6 3v1.5h-3V5H4v1.5H1zM3 7h8l1 5H2z" fill="#0655a3"/><circle cx="7" cy="9.5" r="1.4" fill="#f6bc18"/></svg><span>+41 (0)27 555 01 10</span></li>
    <li><svg viewBox="0 0 14 14"><rect x="3.5" y="1" width="7" height="4" fill="#0655a3"/><rect x="1" y="5" width="12" height="5" rx="1" fill="#0655a3"/><rect x="3.5" y="9" width="7" height="4" fill="#0655a3" stroke="#f6bc18" stroke-width="1"/></svg><span>+41 (0)27 555 01 11</span></li>
    <li><svg viewBox="0 0 14 14"><rect x="1" y="3" width="12" height="8" fill="#0655a3"/><path d="M1 3l6 5 6-5" fill="none" stroke="#f6bc18" stroke-width="1"/></svg><span>info@halvormark-ag.ch</span></li>
    <li><svg viewBox="0 0 14 14" fill="none" stroke="#0655a3" stroke-width="1.2"><circle cx="7" cy="7" r="6"/><ellipse cx="7" cy="7" rx="2.6" ry="6"/><path d="M1 7h12M2 4h10M2 10h10"/></svg><span>www.halvormark-ag.ch</span></li>
  </ul>

  <div class="abs services">
    <span>Architektur</span><span>•</span><span>Verkauf</span><span>•</span><span>Vermietung</span><span>•</span><span>Vermittlung</span><span>•</span><span>Verwaltung</span>
  </div>

  <p class="abs description">Die 2-Zimmer-Wohnung ca. 50 qm Wohn- und Nutzfläche ist komplett möbliert und eingerichtet und kann sofort oder nach Vereinbarung bezogen werden. - Möblierung und Einrichtung müssen nicht miterworben werden. Zur Wohnung gehört ein separates Kellerlokal im UG, sowie ein gedeckter Autoabstellplatz . L’appartement 2 pièces de 50 m2 de surface est complètement meublé, équipé et habitable de suite ou à convenir. L’achat de l’ameublement et de l’équipement n’est pas obligatoire. Avec l’appartement, il y a également une cave individuelle au soussol et une place de parc couverte.</p>

  <h2 class="abs speciality">Speciality:</h2>

  <svg class="abs divider" width="474" height="60" viewBox="0 0 474 60">
    <polygon points="0,4 30,27 0,50" fill="#ec1f27"/>
    <rect x="0" y="26" width="452" height="2" fill="#ec1f27"/>
    <polygon points="378,26 452,26 415,52" fill="#ec1f27"/>
  </svg>

  <div class="abs floorplan">
    <div class="floorplan-area" role="img" aria-label="Grundriss der Wohnung: Bad, Schlafzimmer, Wohn- und Essraum, Balkon"></div>
  </div>

  <div class="abs spine"></div>

  <div class="abs features">
    <div class="feature dark"><div class="feature-label">Rooms:</div><div class="feature-value">2</div></div>
    <div class="feature light"><div class="feature-label">Bathrooms:</div><div class="feature-value">1</div></div>
    <div class="feature dark"><div class="feature-label">Bedrooms:</div><div class="feature-value">1</div></div>
    <div class="feature light"><div class="feature-label">Parking Place:</div><div class="feature-value">1</div></div>
  </div>

  <svg class="abs backdrop" width="710" height="841" viewBox="0 0 710 841">
    <polygon points="0,0 520,0 520,368 192,368 0,498" fill="#0655a3"/>
  </svg>

  <div class="abs photo-main" role="img" aria-label="Hauptbild: Aussicht vom Balkon auf verschneite Berge im Winter"></div>
  <div class="abs photo-bedroom" role="img" aria-label="Foto: Schlafzimmer mit Holzbett und Fenster"></div>
  <div class="abs photo-living" role="img" aria-label="Foto: Wohnraum mit Essbereich und Küchenzeile"></div>
  <div class="abs photo-dining" role="img" aria-label="Foto: Essbereich vor der Balkontür"></div>
  <div class="abs photo-bath" role="img" aria-label="Foto: Badezimmer mit Badewanne"></div>
  <div class="abs photo-hall" role="img" aria-label="Foto: Zimmer mit Holzschrank"></div>

  <div class="abs gold-bar"></div>

  <svg class="abs summary" width="190" height="387" viewBox="0 0 190 387">
    <rect width="190" height="387" fill="#0655a3"/>
    <polygon points="0,150 190,0 190,22 0,172" fill="#ffffff"/>
    <polygon points="0,180 174,42 174,387 0,387" fill="#1f7fc4"/>
  </svg>

  <div class="abs summary-text">
    <div class="category">Appartement</div>
    <div class="year-label">Build Year:</div>
    <div class="year">1996/1997</div>
    <div class="area">50 sqm</div>
    <div class="rule"></div>
    <div class="price">CHF 160’000</div>
  </div>

  <div class="abs side-bar"></div>

</main>
</body>
</html>
```